Jolly Paws Business Card Update

I have a business card which I love. I want to keep the same logo, colours, font and style. I want to upgrade the scripting and remove some elements and add others.
On the front side under Services - remove the existing wording and insert - Providing individual coaching strategies to create happy, healthy and social canine companions
Under Rebecca Thornbury amend the current wording to read: Qualified in Dog Behavioural Training, Natural Animal Healthcare and Animal Health Science
On the reverse side to remove the web address.

```html
<!DOCTYPE html>
<html lang="en">
<head>
<meta charset="utf-8">
<title>Jolly Paws Business Card</title>
<link rel="stylesheet" href="https://fonts.googleapis.com/css2?family=Arimo:wght@400;700&display=swap">
<style>
  :root {
    --page: #ece7df;
    --sky-light: #559bd6;
    --sky-mid: #2f74c4;
    --navy: #0a3b8c;
    --red-bright: #c41316;
    --red-deep: #5e1416;
    --cream: #f4f0d8;
    --ink: #1c1c1c;
    --white: #ffffff;
  }
  * { box-sizing: border-box; margin: 0; padding: 0; }
  html, body {
    width: 1200px; height: 1200px; overflow: hidden;
    background: var(--page);
    font-family: "Arimo", Arial, sans-serif;
  }
  .canvas { position: relative; width: 1200px; height: 1200px; }
  .card {
    position: absolute; left: 150px; width: 900px; height: 500px;
    overflow: hidden;
    box-shadow: 0 6px 18px rgba(0,0,0,0.25);
  }
  .card--front { top: 60px; }
  .card--back { top: 630px; }

  /* front */
  .front-sky {
    position: absolute; left: 0; top: 0; width: 900px; height: 310px;
    background: linear-gradient(180deg, var(--sky-light) 0%, var(--sky-light) 25%, var(--sky-mid) 100%);
  }
  .tagline-band {
    position: absolute; left: 0; top: 310px; width: 900px; height: 30px;
    background: var(--cream); color: var(--ink);
    font-size: 21px; line-height: 30px; text-align: center;
  }
  .front-red {
    position: absolute; left: 0; top: 340px; width: 900px; height: 160px;
    background: linear-gradient(90deg, var(--red-deep) 0%, var(--red-bright) 50%, var(--red-deep) 100%);
  }
  .brand-mark {
    position: absolute; left: 80px; top: 70px; width: 200px; text-align: center;
  }
  .brand-dot {
    width: 110px; height: 110px; border-radius: 50%;
    background: var(--cream); margin: 0 auto 14px;
  }
  .brand-name { color: var(--white); font-size: 30px; font-weight: 700; }
  .divider {
    position: absolute; width: 2px; background: var(--white);
  }
  .divider--services { left: 330px; top: 70px; height: 170px; }
  .services {
    position: absolute; left: 360px; top: 72px; color: var(--white);
  }
  .services-title { font-size: 28px; margin-bottom: 20px; }
  .services-text { font-size: 22px; line-height: 32px; }
  .owner-name {
    position: absolute; left: 200px; top: 358px; width: 320px; text-align: center;
    color: var(--white); font-size: 32px;
  }
  .owner-quals {
    position: absolute; left: 80px; top: 410px; width: 430px; text-align: right;
    color: var(--white); font-size: 20px; line-height: 28px;
  }
  .divider--contact { left: 528px; top: 412px; height: 52px; }
  .contact {
    position: absolute; left: 544px; top: 410px; color: var(--white);
    font-size: 25px; line-height: 30px; list-style: none;
  }
  .contact li { display: flex; align-items: center; gap: 10px; }
  .contact svg { width: 22px; height: 22px; flex: none; }

  /* back */
  .back-sky {
    position: absolute; inset: 0;
    background: linear-gradient(180deg, var(--sky-light) 0%, var(--sky-mid) 50%, var(--navy) 100%);
  }
  .back-mark {
    position: absolute; left: 0; top: 45px; width: 900px; text-align: center;
  }
  .back-mark .brand-dot { width: 190px; height: 190px; margin-bottom: 24px; }
  .back-name { color: var(--cream); font-size: 58px; font-weight: 700; letter-spacing: 2px; }
  .back-tagline {
    color: var(--white); font-size: 26px; margin-top: 8px; letter-spacing: 0.5px;
  }
  .back-wave { position: absolute; left: 0; top: 0; width: 900px; height: 500px; }
</style>
</head>
<body>
<div class="canvas">

  <section class="card card--front">
    <div class="front-sky"></div>
    <div class="brand-mark">
      <div class="brand-dot"></div>
      <div class="brand-name">Jolly Paws</div>
    </div>
    <div class="divider divider--services"></div>
    <div class="services">
      <h2 class="services-title" style="font-weight:400">SERVICES</h2>
      <p class="services-text">Providing individual coaching strategies<br>to create happy, healthy<br>and social canine companions</p>
    </div>
    <div class="tagline-band">Promoting communication and connection between dogs and their families</div>
    <div class="front-red"></div>
    <h1 class="owner-name" style="font-weight:400">Rebecca Thornbury</h1>
    <p class="owner-quals">Qualified in Dog Behavioural Training,<br>Natural Animal Healthcare<br>and Animal Health Science</p>
    <div class="divider divider--contact"></div>
    <ul class="contact">
      <li>
        <svg viewBox="0 0 22 22" aria-hidden="true"><circle cx="11" cy="11" r="10" fill="#fff"/><rect x="7.5" y="5" width="7" height="12" rx="1.2" fill="#8c1416"/><rect x="8.8" y="6.5" width="4.4" height="5" fill="#fff"/></svg>
        0400 127 358
      </li>
      <li>
        <svg viewBox="0 0 22 22" aria-hidden="true"><circle cx="11" cy="11" r="10" fill="#fff"/><rect x="5.5" y="7.5" width="11" height="7.5" fill="none" stroke="#8c1416" stroke-width="1.6"/><path d="M5.5 7.5 L11 12 L16.5 7.5" fill="none" stroke="#8c1416" stroke-width="1.6"/></svg>
        jollypaws1@example.com
      </li>
    </ul>
  </section>

  <section class="card card--back">
    <div class="back-sky"></div>
    <div class="back-mark">
      <div class="brand-dot"></div>
      <div class="back-name">JOLLY PAWS</div>
      <div class="back-tagline">HAPPY DOGS, HAPPY OWNERS</div>
    </div>
    <svg class="back-wave" viewBox="0 0 900 500" aria-hidden="true">
      <defs>
        <linearGradient id="wave-red" x1="0" x2="1" y1="0" y2="0">
          <stop offset="0" stop-color="#5e1416"/>
          <stop offset="0.5" stop-color="#c41316"/>
          <stop offset="1" stop-color="#5e1416"/>
        </linearGradient>
      </defs>
      <path d="M0 425 Q420 370 900 420 L900 500 L0 500 Z" fill="url(#wave-red)"/>
      <path d="M0 425 Q420 370 900 420" fill="none" stroke="#f4f0d8" stroke-width="4"/>
    </svg>
  </section>

</div>
</body>
</html>
```